Modern Website Design for PollMeridian – CX & Loyalty SaaS Platform

We need a modern, professional, and responsive website design for our B2B SaaS platform, PollMeridian. We help companies collect real-time customer feedback, analyze insights, and improve loyalty — combining a powerful CX platform with expert consulting services. The website should clearly communicate who we are and what we offer within the first impression. It should balance data-driven visuals such as dashboards, analytics, and charts with a human, approachable feel. The design must include at least six key pages: Homepage, Product/Services, About, Blog/Resources, Contact/Demo, and Pricing. It should be conversion-focused with clear calls-to-action that encourage visitors to request a demo or contact us. The site must be fully responsive across desktop, tablet, and mobile. It should support multiple languages, starting with English and Danish. Most importantly, the delivery must be a final WordPress website, ready to go live, not just design files.

Target Market(s)

Our target market is medium-to-large B2B organizations. The primary audience includes CX leaders, executives, and managers in customer success and service who want to measure loyalty, understand customer insights, and improve retention.

Industry/Entity Type

Technology / SaaS / Customer Experience

Coding

Coded - Design and coding required

Number of Pages Required

5+ page

Font styles to use
Sans Serif

Requirements
Must have
• The project must deliver a final WordPress website that is fully responsive across all devices. The design should be clean, modern, and SaaS-inspired, with clear calls-to-action on every page. It must also support English and Danish, with a visible language toggle. The site should include visuals of dashboards and analytics that reflect data-driven insights. It must feature sections for case studies or testimonials to build trust. The copywriting should be SEO-friendly, and the design should include smooth animations or hover effects that add polish without making the website feel heavy.
Should not have
• Cluttered layouts, or generic stock photos such as handshakes

```html
<!DOCTYPE html>
<html lang="en">
<head>
<meta charset="utf-8">
<title>PollMeridian – CX &amp; Loyalty Platform</title>
<link href="https://fonts.googleapis.com/css2?family=Montserrat:wght@500;600;700;800&family=Poppins:wght@400;500;600&family=Playfair+Display:ital,wght@1,600&display=swap" rel="stylesheet">
<style>
:root{
  --navy:#1b3a8a;
  --blue:#1d55b8;
  --blue-deep:#12307a;
  --orange:#e8472a;
  --ink:#15183a;
  --text:#3b3f55;
  --muted:#6b6f84;
  --pale:#eef5fd;
  --line:#dde3ee;
  --footer:#15183f;
  --white:#ffffff;
  --star:#f5b301;
}
*{margin:0;padding:0;box-sizing:border-box}
html,body{width:1200px;height:4591px;overflow:hidden}
body{position:relative;background:var(--white);font-family:'Poppins',sans-serif;color:var(--text)}
.abs{position:absolute}
h1,h2,h3,.heading{font-family:'Montserrat',sans-serif;color:var(--ink)}
.btn{position:absolute;display:flex;align-items:center;justify-content:center;border-radius:30px;font-family:'Montserrat',sans-serif;font-weight:600;font-size:12px;letter-spacing:.3px;text-transform:uppercase;transition:transform .2s}
.btn:hover{transform:translateY(-2px)}
.btn-primary{background:linear-gradient(90deg,var(--navy),var(--orange));color:#fff}
.btn-outline{border:1.5px solid #bfc6d6;color:var(--ink);background:#fff}
.btn-white{background:#fff;color:var(--navy)}
.btn-ghost{border:1.5px solid rgba(255,255,255,.8);color:#fff}
.brand{display:flex;align-items:center;gap:8px;font-family:'Montserrat',sans-serif;font-weight:800;color:var(--navy)}
.brand-mark{width:16px;height:16px;background:var(--orange);border-radius:3px}

/* header */
.site-header{position:absolute;top:0;left:0;width:1200px;height:100px;background:#fff;border-bottom:1px solid var(--line)}
.main-nav{position:absolute;left:375px;top:42px;display:flex;gap:20px;font-family:'Montserrat',sans-serif;font-weight:600;font-size:12px;color:var(--ink)}
.lang{position:absolute;left:1014px;top:43px;font-family:'Montserrat',sans-serif;font-size:12px;font-weight:600;color:var(--ink)}
.lang span{color:#9aa0b3;font-weight:500}

/* hero */
.hero{position:absolute;top:100px;left:0;width:1200px;height:590px}
.hero h1{position:absolute;left:143px;top:112px;font-size:44px;line-height:43px;color:#fff;font-weight:600;letter-spacing:.5px}
.hero p{position:absolute;left:143px;top:260px;width:430px;font-size:14px;line-height:23px;color:#e3ebfb}
.dash{position:absolute;left:663px;top:60px;width:560px;height:395px;background:#fff;border-radius:18px;box-shadow:0 20px 40px rgba(10,30,80,.25);border:6px solid #e6ecf6;font-size:8px;color:var(--ink);overflow:hidden}
.dash .tabs{position:absolute;left:165px;top:12px;display:flex;gap:8px}
.dash .tab{padding:5px 12px;border-radius:12px;background:#f1f3f8;font-size:7px}
.dash .tab.on{background:var(--ink);color:#fff}
.dcard{position:absolute;border:1px solid #eceff5;border-radius:10px;background:#fff}
.dcard b{font-weight:500;font-size:9px}
.big{font-size:22px;font-weight:400;font-family:'Poppins',sans-serif}
.trow{position:absolute;left:10px;right:10px;display:flex;justify-content:space-between;align-items:center;font-size:7px;color:var(--muted)}

/* trusted */
.section-title{position:absolute;left:0;width:1200px;text-align:center;font-weight:700}
.section-sub{position:absolute;left:0;width:1200px;text-align:center;font-size:13px;line-height:23px;color:var(--muted)}
.logos{position:absolute;top:817px;left:152px;display:flex;gap:17px}
.logo-box{width:139px;height:76px;border:1px solid var(--line);border-radius:10px;display:flex;align-items:center;justify-content:center;gap:8px;font-family:'Montserrat',sans-serif;font-weight:700;font-size:15px;color:var(--ink);box-shadow:0 4px 10px rgba(20,40,90,.05)}
.logo-box i{width:14px;height:14px;border-radius:50%;background:var(--blue)}

/* features */
.feature{position:absolute;width:287px;height:217px;background:#fff;border-radius:12px;box-shadow:0 6px 22px rgba(20,40,90,.10);text-align:center}
.feature .ic{width:64px;height:64px;margin:20px auto 0;border-radius:12px;background:linear-gradient(135deg,var(--orange),var(--navy));display:flex;align-items:center;justify-content:center}
.feature h3{font-size:17px;margin-top:18px;font-weight:700}
.feature p{font-size:12px;line-height:23px;color:var(--text);margin:6px 18px 0;text-transform:capitalize}

/* about */
.about{position:absolute;top:1756px;left:0;width:1200px;height:590px;background:var(--pale)}
.about p{position:absolute;left:670px;width:402px;font-size:13px;line-height:20.5px;color:var(--text)}
.card-float{position:absolute;background:#fff;border-radius:12px;box-shadow:0 8px 20px rgba(20,40,90,.15)}

/* why */
.why-item{position:absolute;font-family:'Montserrat',sans-serif;font-weight:600;font-size:16px;line-height:21px;color:var(--ink)}
.why-ic{position:absolute;width:68px;height:68px;border-radius:50%;display:flex;align-items:center;justify-content:center;box-shadow:0 0 0 6px rgba(255,255,255,1),0 0 0 7px #e4e9f3}

/* testimonials */
.tcard{position:absolute;width:411px;height:242px;background:#fff;border-radius:8px;box-shadow:0 8px 26px rgba(20,40,90,.12)}
.tphoto{position:absolute;width:112px;height:130px;border-radius:4px}
.tname{position:absolute;font-family:'Montserrat',sans-serif;font-weight:600;font-size:16px;color:var(--ink)}
.tco{position:absolute;font-size:10px;color:var(--muted)}
.stars{position:absolute;color:var(--star);font-size:16px;letter-spacing:3px}
.ttext{position:absolute;font-size:12.5px;line-height:25px;color:var(--text);text-transform:capitalize}
.quote{position:absolute;width:50px;height:76px;background:linear-gradient(180deg,var(--navy),var(--orange));clip-path:polygon(0 0,100% 0,100% 100%,50% 82%,0 100%);color:#fff;font-family:'Montserrat',sans-serif;font-weight:800;font-size:44px;line-height:60px;text-align:center}
.arrow-btn{position:absolute;top:3546px;width:36px;height:36px;border-radius:50%;display:flex;align-items:center;justify-content:center}

/* cta */
.cta{position:absolute;left:143px;top:3750px;width:916px;height:381px;border-radius:42px;background:linear-gradient(135deg,#3d78d6 0%,var(--blue) 45%,var(--blue-deep) 100%)}
.cta h2{position:absolute;left:0;width:1200px;text-align:center;color:#fff;font-weight:600;font-size:42px;line-height:48px}
.cta h2 em{font-family:'Playfair Display',serif;font-style:italic;font-weight:600}

/* footer */
.site-footer{position:absolute;top:4217px;left:0;width:1200px;height:374px;background:var(--footer);color:#fff}
.site-footer h4{position:absolute;font-family:'Montserrat',sans-serif;font-weight:600;font-size:18px}
.flist{position:absolute;font-size:13px;line-height:27px;color:#dfe3f2}
.social{position:absolute;display:flex;align-items:center;gap:12px;font-size:13px;color:#dfe3f2}
.social i{width:28px;height:28px;border-radius:50%;border:1.5px solid #fff;display:inline-block}
.social i.fill{background:var(--orange);border-color:var(--orange)}
</style>
</head>
<body>

<!-- Header -->
<header class="site-header">
  <div class="brand abs" style="left:143px;top:37px;font-size:22px"><span class="brand-mark"></span>PollMeridian</div>
  <nav class="main-nav"><span>PRODUCT</span><span>ABOUT</span><span>RESOURCES</span><span>PRICING</span><span>CONTACT</span></nav>
  <a class="btn btn-primary" style="left:767px;top:29px;width:150px;height:43px">Request a demo</a>
  <a class="btn btn-outline" style="left:925px;top:29px;width:82px;height:43px;border-color:var(--navy)">Login</a>
  <div class="lang">EN | <span>DA</span></div>
</header>

<!-- Hero -->
<section class="hero">
  <svg class="abs" style="left:0;top:0" width="1200" height="590" viewBox="0 0 1200 590">
    <defs>
      <linearGradient id="heroBg" x1="0" y1="0" x2="1" y2="1">
        <stop offset="0" stop-color="#1d5fc4"/>
        <stop offset=".6" stop-color="#1a4aa6"/>
        <stop offset="1" stop-color="#10307c"/>
      </linearGradient>
    </defs>
    <path d="M0 0H1200V380C960 410 640 470 400 568C320 600 220 575 0 470Z" fill="url(#heroBg)"/>
    <path d="M0 330C250 420 420 520 640 400S980 300 1200 330" stroke="rgba(255,255,255,.12)" stroke-width="2" fill="none"/>
    <path d="M0 380C240 470 420 560 660 430S1000 340 1200 360" stroke="rgba(255,255,255,.08)" stroke-width="2" fill="none"/>
  </svg>
  <h1>Transform Customer<br>Feedback Into<br>Actionable Insights</h1>
  <p>PollMeridian combines powerful CX technology with expert consulting to help you understand customers, reduce churn, and drive growth.</p>
  <a class="btn btn-white" style="left:143px;top:349px;width:148px;height:47px">Request a demo</a>
  <a class="btn btn-ghost" style="left:305px;top:349px;width:119px;height:47px">Learn more</a>

  <div class="dash">
    <div class="brand abs" style="left:14px;top:12px;font-size:13px"><span class="brand-mark" style="width:10px;height:10px"></span>PollMeridian</div>
    <div class="tabs"><span class="tab">Overview</span><span class="tab">Operations</span><span class="tab">Security Center</span><span class="tab">Activity</span><span class="tab on">Reports</span></div>

    <div class="dcard" style="left:14px;top:52px;width:180px;height:168px;background:#2b3fe0;border:none;color:#fff">
      <span class="abs" style="left:12px;top:12px;border:1px solid rgba(255,255,255,.6);border-radius:8px;padding:2px 7px;font-size:6px">Findings</span>
      <span class="abs" style="left:12px;top:102px;font-size:12px;line-height:15px;width:150px">Your Transaction Volume has Increased by 5% Since October</span>
    </div>

    <div class="dcard" style="left:204px;top:52px;width:195px;height:150px">
      <b class="abs" style="left:10px;top:12px">Profile Completion</b>
      <span class="abs big" style="left:10px;top:30px">87%</span>
      <span class="abs" style="left:120px;top:44px;font-size:6px;color:var(--muted)">Almost done!</span>
      <div class="abs" style="left:10px;top:66px;width:175px;height:4px;background:#eceff5;border-radius:2px"><div style="width:70%;height:4px;background:linear-gradient(90deg,#2b3fe0,var(--orange));border-radius:2px"></div></div>
      <span class="abs" style="left:10px;top:78px;font-size:6px;color:var(--muted)">Bank details &nbsp;&nbsp;&nbsp; Credit card &nbsp;&nbsp;&nbsp; Other</span>
      <span class="abs" style="left:10px;top:110px;font-size:6px;color:var(--muted)">Secure your account further</span>
      <span class="abs" style="left:10px;top:128px;font-size:6px">Verify email &nbsp;&nbsp;&nbsp;&nbsp; Enable 2FA</span>
    </div>

    <div class="dcard" style="left:410px;top:52px;width:160px;height:178px">
      <b class="abs" style="left:10px;top:12px">Transaction Success Rate</b>
      <span class="abs big" style="left:10px;top:30px">70%</span>
      <span class="abs" style="left:10px;top:60px;font-size:6px;color:var(--muted)">Weekly success rate</span>
      <svg class="abs" style="left:10px;top:90px" width="130" height="60">
        <rect x="0" y="30" width="18" height="28" rx="4" fill="#dfe4f5"/>
        <rect x="22" y="15" width="18" height="43" rx="4" fill="#dfe4f5"/>
        <rect x="44" y="24" width="18" height="34" rx="4" fill="#dfe4f5"/>
        <rect x="66" y="5" width="18" height="53" rx="4" fill="#dfe4f5"/>
        <rect x="88" y="20" width="18" height="38" rx="4" fill="#dfe4f5"/>
      </svg>
      <span class="abs" style="left:10px;top:158px;font-size:6px;color:var(--muted)">Mon &nbsp;&nbsp;&nbsp; Tue &nbsp;&nbsp;&nbsp; Wed &nbsp;&nbsp;&nbsp; Thu</span>
    </div>

    <div class="dcard" style="left:14px;top:230px;width:385px;height:148px">
      <b class="abs" style="left:10px;top:10px">Transaction History</b>
      <span class="abs" style="left:10px;top:24px;font-size:6px;color:var(--muted)">Nov 5 – Nov 7</span>
      <div class="trow" style="top:48px"><span style="color:var(--orange);font-weight:700">■</span><span>Streamly</span><span>7 Nov, 3:20 PM</span><span style="color:#e0a400">• In process</span><span>Subscription</span><span>-$10.00</span></div>
      <div class="trow" style="top:82px"><span style="color:var(--ink);font-weight:700">●</span><span>Photonic</span><span>6 Nov, 12:45 PM</span><span style="color:#e0a400">• In process</span><span>Subscription</span><span>-$19.99</span></div>
      <div class="trow" style="top:116px"><span style="color:var(--ink);font-weight:700">▲</span><span>Pixelbase</span><span>5 Nov, 5:37 PM</span><span style="color:#1ea35a">• Completed</span><span>Subscription</span><span>-$10.00</span></div>
    </div>

    <div class="dcard" style="left:410px;top:240px;width:160px;height:140px">
      <b class="abs" style="left:10px;top:12px">Spending Overview</b>
      <div class="abs" style="left:12px;top:42px;width:36px;height:90px;background:#2b3fe0;border-radius:4px;color:#fff;font-size:7px;padding:4px">67%</div>
      <div class="abs" style="left:54px;top:70px;width:36px;height:62px;background:#e6e9f7;border-radius:4px;font-size:7px;padding:4px">53%</div>
    </div>
  </div>
</section>

<!-- Trusted -->
<h2 class="section-title" style="top:750px;font-size:30px">TRUSTED BY INDUSTRY LEADERS</h2>
<div class="logos">
  <div class="logo-box"><i style="background:var(--orange)"></i>Northwind</div>
  <div class="logo-box"><i></i>Veltrix</div>
  <div class="logo-box"><i style="background:#4658c9"></i>Orbita</div>
  <div class="logo-box"><i style="background:#1a6c74;border-radius:3px"></i>Kestrel</div>
  <div class="logo-box"><i style="background:#5b4bd8;border-radius:3px"></i>Lumora</div>
  <div class="logo-box"><i style="background:#7fc6c9"></i>Pinecrest</div>
</div>

<!-- Features -->
<h2 class="section-title" style="top:975px;font-size:38px">POLLMERIDIAN FEATURES</h2>
<p class="section-sub" style="top:1038px">Get the technology you need and the expertise you want. Our comprehensive approach delivers<br>measurable improvements in customer loyalty and retention.</p>

<div class="feature" style="left:143px;top:1111px">
  <div class="ic"><svg width="34" height="34" viewBox="0 0 34 34" fill="none" stroke="#fff" stroke-width="2.4"><rect x="4" y="6" width="20" height="15" rx="3"/><path d="M9 21l-3 6 7-6"/><circle cx="25" cy="23" r="6"/><path d="M22.5 23l2 2 3.5-4"/></svg></div>
  <h3>Real-Time Feedback</h3>
  <p>Capture customer insights in real-time with customizable surveys and feedback tools.</p>
</div>
<div class="feature" style="left:456px;top:1111px">
  <div class="ic"><svg width="34" height="34" viewBox="0 0 34 34" fill="none" stroke="#fff" stroke-width="2.4"><path d="M17 5a8 8 0 0 0-5 14v4h10v-4A8 8 0 0 0 17 5z"/><path d="M13 27h8M4 30h26"/></svg></div>
  <h3>Expert Consulting</h3>
  <p>Access instant insights with our live dashboards and customizable reports that track key CX metrics.</p>
</div>
<div class="feature" style="left:770px;top:1111px">
  <div class="ic"><svg width="34" height="34" viewBox="0 0 34 34" fill="none" stroke="#fff" stroke-width="2.4"><path d="M17 5L3 29h28z"/><path d="M17 14v7M17 24v2"/></svg></div>
  <h3>Churn-Risk Alerts</h3>
  <p>Access instant insights with our live dashboards and customizable reports that track key CX metrics.</p>
</div>
<div class="feature" style="left:143px;top:1359px">
  <div class="ic"><svg width="34" height="34" viewBox="0 0 34 34" fill="none" stroke="#fff" stroke-width="2.4"><path d="M17 5v12h12A12 12 0 1 1 17 5z"/><path d="M21 3a10 10 0 0 1 10 10H21z"/></svg></div>
  <h3>Segment Insights</h3>
  <p>Dive deep into customer segments to understand different needs and behaviors.</p>
</div>
<div class="feature" style="left:456px;top:1359px">
  <div class="ic"><svg width="34" height="34" viewBox="0 0 34 34" fill="none" stroke="#fff" stroke-width="2.4"><rect x="5" y="5" width="24" height="18" rx="2"/><path d="M10 18v-4M15 18v-8M20 18v-6M25 18v-10M12 29h10M17 23v6"/></svg></div>
  <h3>Leadership Reporting</h3>
  <p>Access ready-to-present reports that highlight key metrics and insights.</p>
</div>
<div class="feature" style="left:770px;top:1359px">
  <div class="ic"><svg width="34" height="34" viewBox="0 0 34 34" fill="none" stroke="#fff" stroke-width="2.4"><path d="M17 29S5 21 5 13a6 6 0 0 1 12-1 6 6 0 0 1 12 1c0 8-12 16-12 16z"/></svg></div>
  <h3>Loyalty Improvement</h3>
  <p>Strengthen customer relationships and build lasting loyalty with actionable insights.</p>
</div>
<a class="btn btn-primary" style="left:458px;top:1624px;width:150px;height:50px">Request a demo</a>
<a class="btn btn-outline" style="left:620px;top:1624px;width:122px;height:50px">Learn more</a>

<!-- About -->
<section class="about">
  <div class="abs" role="img" aria-label="Photo of two colleagues reviewing customer analytics on a tablet" style="left:141px;top:87px;width:367px;height:419px;border-radius:16px;background:linear-gradient(135deg,#5c6a82 0%,#a9b2bf 45%,#dfe2e6 100%)"></div>
  <div class="card-float" style="left:455px;top:129px;width:135px;height:148px">
    <div class="abs" style="left:-14px;top:-14px;width:40px;height:40px;border-radius:50%;background:var(--orange)"></div>
    <span class="abs" style="left:14px;top:40px;font-size:12px;font-weight:500;color:var(--ink)">Sales Analytics</span>
    <span class="abs" style="left:30px;top:62px;font-size:12px;font-weight:600;color:var(--ink)">6.0% ↗</span>
    <svg class="abs" style="left:16px;top:90px" width="110" height="50">
      <rect x="0" y="22" width="8" height="28" rx="3" fill="var(--navy)"/>
      <rect x="16" y="8" width="8" height="42" rx="3" fill="var(--navy)"/>
      <rect x="32" y="30" width="8" height="20" rx="3" fill="var(--orange)"/>
      <rect x="48" y="14" width="8" height="36" rx="3" fill="var(--navy)"/>
      <rect x="64" y="34" width="8" height="16" rx="3" fill="var(--orange)"/>
      <rect x="80" y="6" width="8" height="44" rx="3" fill="var(--navy)"/>
    </svg>
  </div>
  <div class="card-float" style="left:383px;top:401px;width:223px;height:54px;border-radius:27px">
    <span class="abs" style="left:8px;top:11px;width:32px;height:32px;border-radius:50%;background:#8ea3c7;border:2px solid #fff"></span>
    <span class="abs" style="left:30px;top:11px;width:32px;height:32px;border-radius:50%;background:#d8a46d;border:2px solid #fff"></span>
    <span class="abs" style="left:70px;top:9px;color:var(--star);font-size:11px;letter-spacing:2px">★★★★★</span>
    <span class="abs" style="left:70px;top:28px;font-size:9px;color:var(--ink)"><b style="color:#1ea35a;font-weight:600">1.97 based</b> on 23 reviews</span>
    <span class="abs" style="left:178px;top:-20px;width:36px;height:36px;border-radius:50%;background:var(--navy);border:3px solid #fff"></span>
  </div>
  <span class="abs heading" style="left:683px;top:122px;font-size:16px;font-weight:700;color:var(--orange)">ABOUT</span>
  <h2 class="abs" style="left:677px;top:146px;font-size:38px;font-weight:700">POLLMERIDIAN</h2>
  <p style="top:208px">Our mission is to empower businesses with the tools and expertise to build lasting customer relationships. Founded by CX innovators, we combine cutting-edge technology with human insights to drive measurable results.</p>
  <p style="top:298px">With over a decade of experience helping businesses transform their operations, we understand that every organization has unique challenges and goals. Our team of experts works closely with you to deliver solutions that not only meet your current needs but scale with your future growth.</p>
  <a class="btn btn-primary" style="left:675px;top:416px;width:152px;height:48px">Request a demo</a>
  <a class="btn btn-outline" style="left:839px;top:416px;width:121px;height:48px">Learn more</a>
</section>

<!-- Why choose -->
<h2 class="section-title" style="top:2422px;font-size:38px">WHY CHOOSE POLLMERIDIAN?</h2>
<p class="section-sub" style="top:2478px">Discover the features that make our solution the right choice for businesses<br>looking to optimize their workflow and boost productivity.</p>

<svg class="abs" style="left:420px;top:2560px" width="360" height="280" viewBox="0 0 360 280" role="img" aria-label="Connection diagram linking the four benefits">
  <defs>
    <linearGradient id="hub" x1="0" y1="0" x2="1" y2="1"><stop offset="0" stop-color="#1d55b8"/><stop offset="1" stop-color="#e8472a"/></linearGradient>
  </defs>
  <path d="M70 40H108L140 72M290 40H252L220 72M70 236H108L140 204M290 236H252L220 204" stroke="#b9c3d6" stroke-width="1.5" fill="none"/>
  <circle cx="108" cy="40" r="4" fill="#fff" stroke="var(--navy)" stroke-width="2"/>
  <circle cx="252" cy="40" r="4" fill="#fff" stroke="var(--orange)" stroke-width="2"/>
  <circle cx="108" cy="236" r="4" fill="#fff" stroke="var(--navy)" stroke-width="2"/>
  <circle cx="252" cy="236" r="4" fill="#fff" stroke="var(--orange)" stroke-width="2"/>
  <circle cx="180" cy="138" r="96" fill="url(#hub)" opacity=".14"/>
  <circle cx="180" cy="138" r="66" fill="url(#hub)"/>
</svg>

<div class="why-item" style="left:190px;top:2572px;text-align:right;width:182px">The Power Of Software<br>+ Expert Guidance</div>
<div class="why-ic" style="left:389px;top:2566px;background:var(--navy)"><svg width="30" height="30" viewBox="0 0 30 30" fill="none" stroke="#fff" stroke-width="2.2"><rect x="4" y="6" width="22" height="15" rx="2"/><path d="M11 25h8M15 21v4"/></svg></div>
<div class="why-item" style="left:190px;top:2774px;text-align:right;width:185px">Move From Insight To<br>Action, Faster</div>
<div class="why-ic" style="left:389px;top:2762px;background:var(--navy)"><svg width="30" height="30" viewBox="0 0 30 30" fill="none" stroke="#fff" stroke-width="2.2"><path d="M6 24L24 6M14 6h10v10"/><circle cx="8" cy="9" r="3"/></svg></div>
<div class="why-ic" style="left:742px;top:2566px;background:var(--orange)"><svg width="30" height="30" viewBox="0 0 30 30" fill="none" stroke="#fff" stroke-width="2.2"><path d="M15 25S4 18 4 11a5.5 5.5 0 0 1 11-1 5.5 5.5 0 0 1 11 1c0 7-11 14-11 14z"/></svg></div>
<div class="why-item" style="left:830px;top:2572px">Strengthen Relationships<br>At Every Touchpoint</div>
<div class="why-ic" style="left:742px;top:2762px;background:var(--orange)"><svg width="30" height="30" viewBox="0 0 30 30" fill="none" stroke="#fff" stroke-width="2.2"><circle cx="15" cy="15" r="10"/><path d="M18 11h-4a2 2 0 0 0 0 4h2a2 2 0 0 1 0 4h-4M15 8v3M15 19v3"/></svg></div>
<div class="why-item" style="left:824px;top:2774px">Protect Revenue And<br>Reduce Customer Churn</div>

<a class="btn btn-primary" style="left:458px;top:2899px;width:150px;height:50px">Request a demo</a>
<a class="btn btn-outline" style="left:620px;top:2899px;width:122px;height:50px">Learn more</a>

<!-- Testimonials -->
<h2 class="section-title" style="top:3118px;font-size:38px">WHAT OUR CLIENTS SAY</h2>
<p class="section-sub" style="top:3177px">Hear from businesses that have transformed their customer experience with PollMeridian.</p>

<div class="tcard" style="left:173px;top:3258px"></div>
<div class="tphoto" role="img" aria-label="Portrait of client Daniel Reyes" style="left:143px;top:3236px;background:linear-gradient(160deg,#c9cfd8,#8a94a6)"></div>
<div class="tname" style="left:276px;top:3284px">Daniel Reyes</div>
<div class="tco" style="left:276px;top:3310px">Northfield Labs</div>
<div class="stars" style="left:276px;top:3338px">★★★★★</div>
<div class="quote" style="left:522px;top:3256px">”</div>
<div class="ttext" style="left:193px;top:3377px;width:375px">Lorem ipsum is simply dummy texprintintypesettindustry. Lorem ipsum has been the induststanddummy text ever since the 1500s, when an unknown printer togalley of type and scrambled it to make a type</div>

<div class="tcard" style="left:647px;top:3258px"></div>
<div class="tphoto" role="img" aria-label="Portrait of client Clara Voss" style="left:617px;top:3236px;background:linear-gradient(160deg,#d8c3b5,#8c6f63)"></div>
<div class="tname" style="left:752px;top:3284px">Clara Voss</div>
<div class="tco" style="left:752px;top:3310px">Brightwave Group</div>
<div class="stars" style="left:752px;top:3338px">★★★★★</div>
<div class="quote" style="left:996px;top:3256px">”</div>
<div class="ttext" style="left:668px;top:3377px;width:375px">Lorem ipsum is simply dummy texprintintypesettindustry. Lorem ipsum has been the induststanddummy text ever since the 1500s, when an unknown printer togalley of type and scrambled it to make a type</div>

<div class="arrow-btn" style="left:558px;border:1.5px solid var(--ink)"><svg width="16" height="16" viewBox="0 0 16 16" fill="none" stroke="var(--ink)" stroke-width="1.8"><path d="M13 8H3M7 4L3 8l4 4"/></svg></div>
<div class="arrow-btn" style="left:608px;background:linear-gradient(135deg,var(--orange),var(--navy))"><svg width="16" height="16" viewBox="0 0 16 16" fill="none" stroke="#fff" stroke-width="1.8"><path d="M3 8h10M9 4l4 4-4 4"/></svg></div>

<!-- CTA -->
<section class="cta"></section>
<div class="abs" role="img" aria-label="Photo of a team meeting around a laptop" style="left:70px;top:3815px;width:216px;height:216px;transform:rotate(45deg);border-radius:30px;background:linear-gradient(135deg,#6b7a92,#c4ccd6)"></div>
<div class="abs" role="img" aria-label="Photo of a professional working with digital analytics" style="left:880px;top:3940px;width:142px;height:142px;transform:rotate(45deg);border-radius:22px;background:linear-gradient(135deg,#1f3c75,#9fb3cf)"></div>
<div class="cta" style="background:none">
  <h2 style="left:-143px;top:78px">Ready to Transform<br>Your <em>Customer Experience?</em></h2>
  <p class="abs" style="left:0;top:178px;width:916px;text-align:center;color:#e5ecfa;font-size:13px;line-height:22px">See how PollMeridian can help you collect better feedback, gain deeper insights, and<br>drive measurable improvements in customer loyalty.</p>
  <a class="btn btn-white" style="left:342px;top:239px;width:232px;height:46px;color:var(--ink)">Schedule your demo today</a>
</div>

<!-- Footer -->
<footer class="site-footer">
  <div class="brand abs" style="left:143px;top:68px;font-size:34px;color:#fff"><span class="brand-mark" style="width:24px;height:24px"></span>PollMeridian</div>
  <p class="abs" style="left:143px;top:148px;width:290px;font-size:11px;line-height:18px;color:#dfe3f2">Latest Updates, Exclusive Content, And Special Offers? Subscribe To Our Newsletter!</p>
  <div class="abs" style="left:143px;top:191px;width:263px;height:35px;border-radius:18px;background:#fff">
    <span class="abs" style="left:16px;top:9px;font-size:11px;color:#9aa0b3">✉ Your Email</span>
    <span class="abs" style="right:4px;top:4px;width:27px;height:27px;border-radius:50%;background:var(--navy);border:2px solid var(--orange);display:flex;align-items:center;justify-content:center"><svg width="12" height="12" viewBox="0 0 16 16" fill="none" stroke="#fff" stroke-width="2"><path d="M3 8h10M9 4l4 4-4 4"/></svg></span>
  </div>

  <h4 style="left:488px;top:60px">Quick Links</h4>
  <div class="flist" style="left:490px;top:93px">Home<br>Product<br>About<br>Resources<br>Pricing<br>Contact</div>

  <h4 style="left:679px;top:60px">Contact Details</h4>
  <div class="flist" style="left:679px;top:96px;font-size:12.5px;line-height:20px">
    <div style="display:flex;gap:8px"><span>⌖</span><span>48 Harbor Lane, Suite 210<br>Lakeview, OR 97630<br>United States</span></div>
    <div style="display:flex;gap:8px;margin-top:4px"><span>✆</span><span>Phone<br>+1 555 014 2290</span></div>
    <div style="display:flex;gap:8px;margin-top:10px"><span>✉</span><span>Email<br>hello@pollmeridian.com</span></div>
  </div>

  <h4 style="left:940px;top:60px">Social Media</h4>
  <div class="social" style="left:938px;top:100px"><i class="fill"></i>Socialnest</div>
  <div class="social" style="left:938px;top:141px"><i></i>Vidstream</div>
  <div class="social" style="left:938px;top:182px"><i></i>Linkwork</div>
  <div class="social" style="left:938px;top:223px"><i></i>Snapgram</div>

  <div class="abs" style="left:143px;top:312px;width:916px;height:1px;background:rgba(255,255,255,.2)"></div>
  <span class="abs" style="left:143px;top:338px;font-size:12px;color:#dfe3f2">© 2025 PollMeridian. All Rights Reserved.</span>
  <span class="abs" style="left:843px;top:338px;font-size:12px;color:#dfe3f2">Privacy Policy &nbsp;|&nbsp; Terms Of Service</span>
</footer>

</body>
</html>
```